Redesign Buch-/eBook-Cover
Zielgruppe
Ich bin Hobbyautor.
Aufgabenstellung
Ich suche ein Design für mein erstes, bisher unveröffentlichtes Buch. Dieses habe ich ursprünglich 2008 geschrieben und dafür mit meinen wenig ausgeprägten Grafikkünsten ein eigenes Cover erstellt. Nun habe ich dieses Buch in den letzen 1,5 Jahren neu geschrieben, plane nun eine Veröffentlichung und suche einen Designer, der meinen amateurhaften Entwurf in einen künstlerisch ansprechenden verwandelt.
- benötigt wird Front, Buchrücken und Rückseite. Das Format ist DIN A5
- ich möchte, daß Weiß die dominierende Farbe ist, damit der rote Blutfleck besonders gut zur Geltung kommt.
- das Weiß muss nicht rein sein, sondern kann auch gerne eine Struktur aufweisen. Deshalb habe ich ein von mir in Blender erstelltes
Render eines Mauerwerks mit hochgeladen, daß gerne verwendet werden kann/soll.
- der Titel lautet MCDXLII, das ist die römische Schreibweise der Zahl 666, der Titel muss NICHT eingerahmt sein. Hier gilt künstlerische Freiheit.
- ich stelle mir die Verwendung eines okkulten/satanistischen, auf dem Kopf stehenden Pentagrams mit eventuellem Bockschädel vor, wie man es im Internet häufig findet.
- mein Cover besteht aus Grafiken, die ich achtlos aus dem Internet geladen habe und ich besitze KEINE Rechte daran.
- ich wünsche mir eine moderne, künstlerische Interpretation meines ursprünglichen Covers.
- sehr wichtig ist für mich das Blut. Es soll so wirken, als wäre das Pentagramm damit bespritzt worden und läuft dann daran und/oder an der Wand herunter.
- der Buchtitel kann ruhig kleiner als auf meinem Cover sein, dafür das Pentagram größer.
- lassen Sie Ihrer Kreativität freien Lauf, ich freue mich auf Ihr Design.

```html
<!DOCTYPE html>
<html lang="de">
<head>
<meta charset="utf-8">
<title>MCDXLII – Buchcover</title>
<link rel="stylesheet" href="https://fonts.googleapis.com/css2?family=Marcellus&family=Pirata+One&family=Cinzel:wght@400&family=Libre+Baskerville:wght@700&family=Poppins:wght@400&display=swap">
<style>
  :root {
    --stage: #7b8a8b;
    --wall: #f1f1ef;
    --wall-shade: #e2e2df;
    --blood: #b7202e;
    --blood-dark: #8e1520;
    --ink: #1b1b1b;
    --paper-white: #ffffff;
  }
  * { margin: 0; padding: 0; box-sizing: border-box; }
  html, body { width: 1200px; height: 2188px; overflow: hidden; }
  body { background: var(--stage); position: relative; font-family: "Poppins", sans-serif; }

  .cover-front {
    position: absolute;
    container-type: inline-size;
    background: linear-gradient(180deg, var(--wall) 0%, var(--wall-shade) 100%);
    overflow: hidden;
  }
  .cover-front--single { left: 220px; top: 120px; width: 760px; height: 1075px; box-shadow: 0 30px 40px rgba(0,0,0,.25); }

  .author-name {
    position: absolute; top: 5.5%; left: 0; right: 0; text-align: center;
    font-family: "Marcellus", serif; font-size: 5cqw; letter-spacing: .02em; color: var(--ink);
  }
  .occult-artwork {
    position: absolute; left: 3%; right: 1%; top: 15%; bottom: 0;
    background:
      radial-gradient(ellipse 46% 38% at 50% 42%, rgba(255,255,255,.9) 0%, rgba(247,226,220,.85) 55%, rgba(183,32,46,.55) 78%, rgba(183,32,46,0) 92%),
      linear-gradient(180deg, rgba(183,32,46,0) 55%, var(--blood) 80%, var(--blood-dark) 100%);
  }
  .book-title {
    position: absolute; left: 0; right: 0; top: 71%; text-align: center;
    font-family: "Pirata One", serif; font-size: 17cqw; line-height: 1; color: var(--paper-white);
    letter-spacing: .02em;
  }
  .genre-label {
    position: absolute; left: 22%; top: 87.5%;
    font-family: "Cinzel", serif; font-size: 5cqw; color: var(--paper-white);
  }

  .cover-spread {
    position: absolute; left: 82px; top: 1385px; width: 1036px; height: 705px;
    display: flex; background: linear-gradient(180deg, var(--wall) 0%, var(--wall-shade) 100%);
    box-shadow: 0 12px 20px rgba(0,0,0,.2);
  }
  .cover-back { width: 490px; height: 100%; position: relative; padding: 0 46px; }
  .back-emblem {
    position: absolute; left: 50%; top: 58px; width: 130px; height: 130px; margin-left: -65px;
    border-radius: 50%;
    background: radial-gradient(circle, rgba(255,255,255,.95) 30%, rgba(183,32,46,.45) 70%, rgba(183,32,46,0) 100%);
  }
  .back-headline {
    position: absolute; top: 220px; left: 46px; right: 46px; text-align: center;
    font-family: "Libre Baskerville", serif; font-weight: 700; font-size: 15px; line-height: 1.35;
    color: var(--blood); text-transform: uppercase;
  }
  .back-blurb {
    position: absolute; top: 300px; left: 68px; right: 50px;
    font-size: 11px; line-height: 1.42; color: var(--ink); text-align: justify;
  }
  .back-blurb p + p { margin-top: 14px; }

  .book-spine { width: 40px; height: 100%; position: relative; }
  .spine-text {
    position: absolute; left: 50%; top: 50%; white-space: nowrap;
    transform: translate(-50%, -50%) rotate(-90deg);
    font-family: "Poppins", sans-serif; font-size: 12px; letter-spacing: .04em; color: var(--ink);
  }
  .spine-dot { display: inline-block; width: 6px; height: 6px; border-radius: 50%; background: var(--blood); margin: 0 6px; vertical-align: middle; }

  .cover-front--spread { position: relative; width: 506px; height: 100%; }
</style>
</head>
<body>

  <section class="cover-front cover-front--single">
    <div class="author-name">OLAF BRUNNHUBER</div>
    <div class="occult-artwork" role="img" aria-label="Roter Bockschädel vor umgedrehtem Pentagramm im Runenkreis, von Blut bespritzt, das an der Wand herunterläuft"></div>
    <div class="book-title">MCDXLII</div>
    <div class="genre-label">THRILLER</div>
  </section>

  <section class="cover-spread">
    <div class="cover-back">
      <div class="back-emblem" role="img" aria-label="Kleiner roter Bockschädel mit Pentagramm"></div>
      <h2 class="back-headline">Lorem ipsum dolor sit amet, consectetur adipiscing elit in a elit nec tortor euismod suscipit.</h2>
      <div class="back-blurb">
        <p>Nulla in massa vel sem hendrerit condimentum at nec elit Sed nec imperdiet enim. Curabitur id scelerisque nibh. Aliquam iaculis eros et est faucibus iaculis. Aliquam blandit magna neque, sit amet scelerisque ex consectetur Vestibulum euismod pharetra justo. Praesent tristique accumsan ornare. Quisque nec lacinia dui. Suspendisse aliquet ipsum nec risus congue dapibus.</p>
        <p>Proin et volutpat velit, sit amet porttitor ex. Maecenas et enim id leo accumsan mollis. Proin et nisi ac urna congue posuere sed eu orci. Maecenas pulvinar orci tellus, sed tempor neque sodales id. Nulla id lacinia ante, id elementum neque. Sed pretium in velit eget malesuada. Vestibulum lacinia cursus massa vel fringilla. Vivamus euismod tortor turpis, vel ultricies libero convallis eget. Donec condimentum quam et orci vehicula efficitur. Pellentesque habitant morbi tristique senectus et netus et malesuada fames ac turpis egestas. Donec ullamcorper, mauris sed condimentum pulvinar, felis risus tincidunt quam, non vestibulum tellus enim sit amet diam.</p>
      </div>
    </div>

    <div class="book-spine">
      <div class="spine-text">MCDXLII<span class="spine-dot"></span>OLAF BRUNNHUBER</div>
    </div>

    <div class="cover-front cover-front--spread">
      <div class="author-name">OLAF BRUNNHUBER</div>
      <div class="occult-artwork" role="img" aria-label="Roter Bockschädel vor umgedrehtem Pentagramm im Runenkreis, von Blut bespritzt, das an der Wand herunterläuft"></div>
      <div class="book-title">MCDXLII</div>
      <div class="genre-label">THRILLER</div>
    </div>
  </section>

</body>
</html>
```